Flyer-Design TorvelMax Endkunde
Zielgruppe
Die Online-Plattform TorvelMax vermittelt dem Endkunden einen ServicePartner bei welchem er seine beschädigten Felgen professionell nach vorgegebenen gesetzlichen Richtlinien reparieren bzw. aufbereiten lassen kann. Ganz ohne großen Aufwand für den Kunden und zu erschwinglichen Preisen. Zielgruppe sind also Fahrzeugbesitzer mit beschädigten Alufelgen.
Aufgabenstellung
Design soll einen Wiedererkennungswert zur Website www.torvelmax.com (Bitte direkt in die Browser Suche eingeben, Website ist erst seit heute online) darstellen. Der Flyer wird von den ServicePartnern zur Kundenansprache verwendet.
Texte siehe pdf.
Auf der Website verwendetes Bildmaterial kann zur Verfügung gestellt werden. Sonst gerne Alternativ-Vorschläge für Stock-Fotos.
TorvelMax Logo und Styleguide siehe Anhang.

```html
<!DOCTYPE html>
<html lang="de">
<head>
<meta charset="utf-8">
<title>TorvelMax – Flyer Endkunde</title>
<link rel="stylesheet" href="https://fonts.googleapis.com/css2?family=Open+Sans:ital,wght@0,400;0,700;0,800;1,700;1,800&display=swap">
<style>
  :root {
    --brand-red: #c01825;
    --ink: #1a1a1a;
    --white: #ffffff;
    --stripe: rgba(255,255,255,0.82);
    --box-grey: #9a9a9a;
    --ring-grey: #8e8e8e;
  }
  * { margin: 0; padding: 0; box-sizing: border-box; }
  html, body { width: 1200px; height: 1199px; overflow: hidden; }
  body { font-family: "Open Sans", Arial, sans-serif; background: var(--white); }
  .flyer { position: relative; width: 1200px; height: 1199px; overflow: hidden; background: var(--brand-red); }

  .hero-photo {
    position: absolute; left: 0; top: 0; width: 1200px; height: 494px;
    background: linear-gradient(100deg, #dfe5ea 0%, #eef1f3 35%, #f4f4f4 45%, #5d6168 58%, #3c3f45 75%, #e9e9e9 88%, #cfd2d5 100%);
  }
  .stripes { position: absolute; left: 0; top: 0; width: 1200px; height: 540px; }

  .detail-photo {
    position: absolute; width: 318px; height: 318px; border-radius: 50%;
    border: 7px solid var(--ring-grey);
  }
  .detail-photo.tyre { left: 516px; top: 273px; background: radial-gradient(circle at 40% 45%, #d9d9d9 0%, #6b6b6b 45%, #3a3a3a 70%, #a3202a 100%); }
  .detail-photo.repair { left: 857px; top: 273px; background: radial-gradient(circle at 40% 40%, #f2f2f2 0%, #4a4a4a 35%, #2b2b2b 70%, #8a8a8a 100%); }

  .brand-mark {
    position: absolute; left: 150px; top: 150px;
    display: flex; align-items: center; gap: 12px;
  }
  .brand-mark .dot { width: 40px; height: 40px; border-radius: 50%; background: var(--brand-red); }
  .brand-mark .name { font-weight: 800; font-size: 42px; color: var(--brand-red); }

  .headline {
    position: absolute; left: 58px; top: 232px;
    color: var(--brand-red); font-weight: 800; font-size: 50px; line-height: 48px;
  }
  .headline em { font-style: italic; display: block; }
  .tagline {
    position: absolute; left: 57px; top: 346px; width: 440px;
    color: var(--ink); font-weight: 800; font-style: italic; font-size: 22.5px; line-height: 25px;
  }

  .copy { position: absolute; left: 0; top: 600px; width: 1200px; color: var(--white); }
  .copy .lead {
    position: absolute; left: 29px; top: 0; font-weight: 700; font-size: 21px; line-height: 28px;
    display: flex; gap: 17px; align-items: center; white-space: nowrap;
  }
  .copy .lead svg { width: 18px; height: 22px; }
  .copy p { position: absolute; left: 67px; width: 1090px; font-size: 20.6px; line-height: 26.5px; }

  .contact-box {
    position: absolute; left: 76px; top: 1035px; width: 1053px; height: 141px;
    background: var(--box-grey); border: 6px solid var(--white); border-radius: 16px;
    color: var(--white); font-weight: 700; font-size: 24px; line-height: 30px;
    padding: 14px 0 0 31px;
  }
  .contact-box .legal { margin-top: 15px; }
</style>
</head>
<body>
<div class="flyer">
  <div class="hero-photo" role="img" aria-label="Foto: weißes Auto mit dunkler Speichen-Alufelge und roter Bremse in heller Werkstatt"></div>

  <svg class="stripes" viewBox="0 0 1200 540" aria-hidden="true">
    <g fill="var(--stripe)">
      <polygon points="18,450 48,450 76,494 48,535 18,535 46,494"/>
      <polygon points="94,450 124,450 152,494 124,535 94,535 122,494"/>
      <polygon points="170,450 200,450 228,494 200,535 170,535 198,494"/>
      <polygon points="246,450 276,450 304,494 276,535 246,535 274,494"/>
      <polygon points="322,450 352,450 380,494 352,535 322,535 350,494"/>
      <polygon points="398,450 428,450 456,494 428,535 398,535 426,494"/>
      <polygon points="474,450 504,450 532,494 504,535 474,535 502,494"/>
      <polygon points="550,450 580,450 608,494 580,535 550,535 578,494"/>
      <polygon points="838,450 868,450 896,494 868,535 838,535 866,494"/>
      <polygon points="1158,318 1178,318 1195,357 1178,397 1158,397 1175,357"/>
    </g>
  </svg>

  <div class="detail-photo tyre" role="img" aria-label="Nahaufnahme: Bordsteinschaden am Felgenhorn neben dem Reifen"></div>
  <div class="detail-photo repair" role="img" aria-label="Nahaufnahme: Hand mit Handschuh prüft beschädigte schwarze Felge"></div>

  <div class="brand-mark">
    <span class="dot"></span>
    <span class="name">TorvelMax</span>
  </div>

  <h1 class="headline">Felge beschädigt?<em>Wie ärgerlich!</em></h1>
  <p class="tagline">Experten schätzen, dass rund jede vierte Alufelge auf Deutschlands Straßen beschädigt ist.</p>

  <section class="copy">
    <div class="lead">
      <svg viewBox="0 0 18 22" aria-hidden="true"><polygon points="0,0 8,0 18,11 8,22 0,22 10,11" fill="var(--white)"/></svg>
      <span>Ihre Alufelge(n) gehören auch dazu? Dann haben wir eine schnelle und fachgerechte Lösung für Sie.</span>
    </div>
    <p style="top:48px">Denn nichts geht über eine schöne Felge, die das Erscheinungsbild Ihres Autos erst abrundet.</p>
    <p style="top:101px">Als geprüfter TorvelMax ServicePartner bieten wir Ihnen die Möglichkeit Ihre beschädigte(n) Alufelge(n) ganz einfach über uns instandsetzen zu lassen. Ohne viel Aufwand für Sie erstrahlen Ihre Felge(n) "in neuem Glanz".</p>
    <p style="top:207px">Selbstverständlich steht eine optisch einwandfreie Aufbereitung stringent nach allen rechtlichen Vorgaben dabei für uns an erster Stelle.</p>
    <p style="top:286px">Gleich ob, silberne, farbig lackierte, glanzgedrehte oder Luxus-Felgen – Wir bieten Ihnen mit einem innovativen und zukunftsweisenden Verfahren unter Einhaltung strenger Qualitäts- und Reparaturstandards die perfekte Lösung für das „zweite“ Leben Ihrer Alufelge(n)!</p>
    <p style="top:385px">- Und das Beste daran: Zu einem absolut fairen Preis!</p>
  </section>

  <div class="contact-box">
    <div>Sie haben Fragen? Als TorvelMax ServicePartner beraten Sie gerne!</div>
    <div>www.torvelmax.com</div>
    <div class="legal">© BrisoLark GmbH | Lindauer Weg 12 | 84123 Gerstenau bei Tannfeld</div>
  </div>
</div>
</body>
</html>
```